glow 742 is renewing its image

more dynamic website, make it look more attractive for the services we offer, at the same time more accurate on the services description. We want people to know we offer treatments that big corporations offer but not as expensive as they offer it. prices will be add by me once the website is approve
Updates

already have a website with wix.com www.glow742dermis.com

Target Market(s)

women between 21 to 75

Industry/Entity Type

beauty services, body contouring

Colors

Designer to choose colors to be used in the design.

Requirements
Must have
• pictures of treatments
Nice to have
• accurate information about treatmnets, treatments menu
Should not have
• no online shopping

```html
<!DOCTYPE html>
<html lang="en">
<head>
<meta charset="utf-8">
<title>Glow 742 Skin Lounge – Ultrasound Cavitation</title>
<link href="https://fonts.googleapis.com/css2?family=Roboto:wght@300;400;500;700&display=swap" rel="stylesheet">
<style>
  :root{
    --blush:#fde4e1;
    --tan:#d1a677;
    --tan-line:#dcb9a0;
    --ink:#2b2b2b;
    --white:#ffffff;
    --footer:#333333;
    --photo-cool-a:#eef1f6;
    --photo-cool-b:#9fb8de;
    --photo-warm-a:#f3e6dc;
    --photo-warm-b:#c9a58e;
  }
  *{margin:0;padding:0;box-sizing:border-box}
  html,body{width:1200px;height:3478px;overflow:hidden}
  body{position:relative;background:var(--white);font-family:'Roboto',sans-serif;color:var(--ink)}
  .abs{position:absolute}

  .hero{left:0;top:0;width:1200px;height:813px;background:var(--blush)}
  .brand{left:122px;top:38px;font-family:'Roboto',sans-serif;font-weight:300;font-size:44px;color:var(--tan);letter-spacing:1px}
  .brand-footer{left:122px;top:3035px;color:var(--white)}
  .nav a{position:absolute;top:56px;font-size:12px;color:var(--ink);text-decoration:none}

  .arch-frame{border:1px solid var(--tan-line);border-radius:999px 999px 0 0}
  .arch-photo{border-radius:999px 999px 0 0}
  .hero-frame{left:369px;top:112px;width:461px;height:587px}
  .hero-photo{left:381px;top:124px;width:437px;height:562px;background:linear-gradient(160deg,var(--photo-cool-a) 30%,var(--photo-cool-b))}

  .page-title{left:761px;top:286px;font-size:32px;font-weight:300;color:var(--tan)}
  .breadcrumb{left:203px;top:420px;font-size:18px;color:var(--ink)}

  .booking{height:63px;background:var(--white);border-radius:32px;box-shadow:0 4px 14px rgba(0,0,0,.08);display:flex;align-items:center}
  .booking .price{flex:1;text-align:center;font-size:12px;font-weight:500;color:var(--ink)}
  .booking .cta{height:63px;background:var(--tan);border-radius:32px;color:var(--white);font-size:12px;font-weight:700;display:flex;align-items:center;justify-content:center}
  .booking-hero{left:698px;top:518px;width:386px}
  .booking-hero .cta{width:248px}
  .booking-body{left:406px;top:2047px;width:388px}
  .booking-body .cta{width:250px}

  .article{left:273px;top:937px;width:654px;text-align:center;font-size:19px;line-height:28px;color:var(--ink)}
  .article p{margin-bottom:28px}
  .article h2{font-size:19px;font-weight:500;line-height:28px}
  .article .gap{margin-top:56px}

  .newsletter{left:0;top:2233px;width:1200px;height:675px;background:var(--blush)}
  .news-frame{left:169px;top:2309px;width:412px;height:523px}
  .news-photo{left:181px;top:2319px;width:387px;height:501px;background:linear-gradient(150deg,var(--photo-warm-b),var(--photo-warm-a) 55%)}
  .news-heading{left:644px;top:2478px;font-size:32px;font-weight:300;line-height:44px;color:var(--tan)}
  .signup{left:644px;top:2600px;width:387px}
  .signup .field{flex:1;padding-left:31px;font-size:12px;color:var(--ink)}
  .signup .cta{width:124px}

  .footer{left:0;top:2908px;width:1200px;height:570px;background:var(--footer);color:var(--white)}
  .about-text{left:119px;top:3128px;width:250px;font-size:12px;line-height:18.5px;color:var(--white)}
  .about-text p{margin-bottom:18.5px}
  .footer-heading{top:3060px;font-size:18px;font-weight:500;color:var(--white)}
  .quick-links{left:598px;top:3112px;list-style:none}
  .quick-links li{font-size:12px;line-height:25px}
  .social{top:3108px;width:51px;height:51px;border-radius:50%;background:var(--white)}
</style>
</head>
<body>
  <section class="abs hero"></section>
  <div class="abs brand">Glow 742</div>
  <nav class="nav">
    <a style="left:788px">Home</a>
    <a style="left:868px">Services</a>
    <a style="left:961px">About</a>
    <a style="left:1041px">Contact</a>
  </nav>

  <div class="abs arch-frame hero-frame"></div>
  <div class="abs arch-photo hero-photo" role="img" aria-label="Gloved hand holding an ultrasound cavitation handpiece"></div>
  <h1 class="abs page-title">Ultrasound Cavitation</h1>
  <div class="abs breadcrumb">Services &gt; Body Treatments</div>
  <div class="abs booking booking-hero">
    <span class="price">$79 per Session</span>
    <span class="cta">BOOK A SESSION NOW</span>
  </div>

  <article class="abs article">
    <p>Ultrasonic or ultrasound cavitation is uisque sed leo sodales sem molestie lacinia. Nam ultrices nulla a tempor lacinia. Donec vitae dictum lorem, et suscipit lorem. Ut mattis enim ipsum, ac tincidunt augue laoreet nec. Nunc sed quam vehicula, ultricies arcu at, congue tortor. Sed sed facilisis metus, eu consequat turpis. Suspendisse cursus dignissim sapien, at congue leo semper nec.</p>
    <h2>How Does it Work?</h2>
    <p>Wuisque sed leo sodales sem molestie lacinia. Nam ultrices nulla a tempor lacinia. Donec vitae dictum lorem, et suscipit lorem. Ut mattis enim ipsum, ac tincidunt augue laoreet nec. Nunc sed quam vehicula, ultricies arcu at, congue tortor. Sed sed facilisis metus, eu consequat turpis. Suspendisse cursus dignissim sapien, at congue leo semper nec.</p>
    <h2>How long do ultrasonic cavitation sessions last?</h2>
    <p>Ruisque sed leo sodales sem molestie lacinia. Nam ultrices nulla a tempor lacinia. Donec vitae dictum lorem, et suscipit lorem. Ut mattis enim ipsum, ac tincidunt augue laoreet nec. Nunc sed quam vehicula, ultricies arcu at, congue tortor. Sed sed facilisis metus, eu consequat turpis. Suspendisse cursus dignissim sapien, at congue leo semper nec.</p>
    <h2>Which body parts are best for ultrasonic cavitation?</h2>
    <p>Euisque sed leo sodales sem molestie lacinia. Nam ultrices nulla a tempor lacinia. Donec vitae dictum lorem, et suscipit lorem. Ut mattis enim ipsum, ac tincidunt augue laoreet nec. Nunc sed quam vehicula, ultricies arcu at, congue tortor. Sed sed facilisis metus, eu consequat turpis. Suspendisse cursus dignissim sapien, at congue leo semper nec.</p>
    <h2 class="gap" style="font-weight:400">Health Impacts of Ultrasonic Cavitation</h2>
    <p>Huisque sed leo sodales sem molestie lacinia. Nam ultrices nulla a tempor lacinia. Donec vitae dictum lorem, et suscipit lorem. Ut mattis enim ipsum, ac tincidunt augue laoreet nec. Nunc sed quam vehicula, ultricies arcu at, congue tortor. Sed sed facilisis metus, eu consequat turpis. Suspendisse cursus dignissim sapien, at congue leo semper nec.</p>
  </article>

  <div class="abs booking booking-body">
    <span class="price">$79 per Session</span>
    <span class="cta">BOOK A SESSION NOW</span>
  </div>

  <section class="abs newsletter"></section>
  <div class="abs arch-frame news-frame"></div>
  <div class="abs arch-photo news-photo" role="img" aria-label="Portrait of a woman with glowing skin holding a flower to her cheek"></div>
  <h2 class="abs news-heading">Get the latest updates and<br>receive exclusive discounts.</h2>
  <div class="abs booking signup">
    <span class="field">Your Email Address</span>
    <span class="cta">SUBMIT</span>
  </div>

  <footer class="abs footer"></footer>
  <div class="abs brand brand-footer">Glow 742</div>
  <div class="abs about-text">
    <p>At Glow 742 Skin Lounge we provide high quality skin and body treatments that will make you look great and feel great!</p>
    <p>With more than 10 years of experience our Esthetician Marisol will provide you with the information and the treatment that is right for you and your budget.</p>
    <p>We are like your personal assistants but for your beauty. You can always call us if you have any questions.</p>
  </div>
  <h3 class="abs footer-heading" style="left:598px">Quick Links</h3>
  <ul class="abs quick-links">
    <li>Services</li>
    <li>About</li>
    <li>Contact</li>
    <li>Reservation Policy</li>
    <li>Cancellation Policy</li>
  </ul>
  <h3 class="abs footer-heading" style="left:869px">Follow Us</h3>
  <div class="abs social" style="left:869px" aria-label="Social profile"></div>
  <div class="abs social" style="left:938px" aria-label="Social profile"></div>
</body>
</html>
```